banner ad

We're looking for a banner similar to the one shown on the attached file. The same 4 keywords, the same text up top, but with new formatting, design and perhaps color scheme. Looking for something to catch people's attention that will stand out on this particular page shown in the attached image. Our goal is to find a banner with a better click through rate than the current version.

```html
<!DOCTYPE html>
<html lang="en">
<head>
<meta charset="utf-8">
<title>Ads Related to Blood Glucose</title>
<link rel="stylesheet" href="https://fonts.googleapis.com/css2?family=Bebas+Neue&display=swap">
<style>
  :root {
    --navy-deep: #0c1633;
    --navy: #16265a;
    --ink: #12204a;
    --white: #ffffff;
    --accent: #ffd23f;
    --muted: #b9c3e6;
    --coral: #ff5a5f;
    --coral-dark: #e23d52;
    --teal: #00b8a9;
    --teal-dark: #00897f;
    --amber: #ffa62b;
    --amber-dark: #f07b12;
    --violet: #7b61ff;
    --violet-dark: #5a3fe0;
    --card-shadow: rgba(0, 0, 0, 0.35);
  }
  * { margin: 0; padding: 0; box-sizing: border-box; }
  html, body { width: 1200px; height: 277px; overflow: hidden; }
  body { font-family: "Bebas Neue", "Oswald", sans-serif; background: var(--navy-deep); }

  .banner {
    position: relative;
    width: 1200px; height: 277px;
    background:
      radial-gradient(circle at 8% 20%, rgba(123, 97, 255, 0.35) 0%, rgba(123, 97, 255, 0) 45%),
      radial-gradient(circle at 95% 100%, rgba(0, 184, 169, 0.30) 0%, rgba(0, 184, 169, 0) 45%),
      linear-gradient(120deg, var(--navy-deep) 0%, var(--navy) 100%);
    overflow: hidden;
  }

  .headline {
    position: absolute;
    left: 40px; top: 0; bottom: 0;
    width: 230px;
    display: flex;
    flex-direction: column;
    justify-content: center;
    font-weight: 400;
  }
  .headline-kicker {
    color: var(--muted);
    font-size: 32px;
    line-height: 1;
    letter-spacing: 3px;
  }
  .headline-rule {
    width: 56px; height: 6px;
    margin: 10px 0 12px;
    border-radius: 3px;
    background: var(--accent);
  }
  .headline-main {
    color: var(--white);
    font-size: 70px;
    line-height: 0.88;
    letter-spacing: 1px;
  }
  .headline-main .hl { color: var(--accent); }

  .keyword-grid {
    position: absolute;
    left: 296px; top: 28px;
    width: 876px; height: 221px;
    display: grid;
    grid-template-columns: 1fr 1fr;
    grid-template-rows: 1fr 1fr;
    gap: 17px 20px;
  }
  .keyword {
    display: flex;
    align-items: center;
    gap: 18px;
    padding: 0 16px 0 12px;
    border-radius: 16px;
    background: var(--white);
    box-shadow: 0 8px 18px var(--card-shadow);
    text-decoration: none;
    color: var(--ink);
  }
  .keyword-tile {
    flex: none;
    width: 80px; height: 80px;
    border-radius: 14px;
    display: flex;
    align-items: center;
    justify-content: center;
  }
  .keyword-tile svg { width: 50px; height: 50px; }
  .keyword-label {
    flex: 1;
    font-size: 35px;
    line-height: 0.95;
    letter-spacing: 0.5px;
  }
  .keyword-go {
    flex: none;
    width: 48px; height: 48px;
    border-radius: 50%;
    display: flex;
    align-items: center;
    justify-content: center;
  }
  .keyword-go svg { width: 22px; height: 22px; }

  .glucose .keyword-tile, .glucose .keyword-go { background: linear-gradient(135deg, var(--coral), var(--coral-dark)); }
  .range .keyword-tile, .range .keyword-go { background: linear-gradient(135deg, var(--teal), var(--teal-dark)); }
  .chart .keyword-tile, .chart .keyword-go { background: linear-gradient(135deg, var(--amber), var(--amber-dark)); }
  .normal .keyword-tile, .normal .keyword-go { background: linear-gradient(135deg, var(--violet), var(--violet-dark)); }
</style>
</head>
<body>
<div class="banner">
  <h1 class="headline">
    <span class="headline-kicker">Ads Related To</span>
    <span class="headline-rule" aria-hidden="true"></span>
    <span class="headline-main">Blood<br><span class="hl">Glucose</span></span>
  </h1>

  <nav class="keyword-grid">
    <a class="keyword glucose" href="#">
      <span class="keyword-tile">
        <svg viewBox="0 0 50 50" fill="none" stroke="#fff" stroke-width="2.4" aria-hidden="true">
          <circle cx="19" cy="9" r="3.5"/><circle cx="31" cy="9" r="3.5"/>
          <circle cx="13" cy="19" r="3.5"/><circle cx="25" cy="19" r="3.5"/><circle cx="37" cy="19" r="3.5"/>
          <circle cx="9" cy="30" r="3.5"/><circle cx="21" cy="30" r="3.5"/><circle cx="33" cy="30" r="3.5"/><circle cx="43" cy="30" r="3.5"/>
          <circle cx="15" cy="41" r="3.5"/><circle cx="27" cy="41" r="3.5"/><circle cx="38" cy="41" r="3.5"/>
        </svg>
      </span>
      <span class="keyword-label">Blood<br>Glucose</span>
      <span class="keyword-go"><svg viewBox="0 0 22 22" fill="none" stroke="#fff" stroke-width="3" stroke-linecap="round" stroke-linejoin="round" aria-hidden="true"><path d="M4 11h13M12 5l6 6-6 6"/></svg></span>
    </a>

    <a class="keyword range" href="#">
      <span class="keyword-tile">
        <svg viewBox="0 0 50 50" fill="none" stroke="#fff" stroke-width="2.6" stroke-linejoin="round" aria-hidden="true">
          <path d="M6 4V44H46"/>
          <polyline points="14,34 23,22 32,28 42,12"/>
          <circle cx="14" cy="34" r="3" fill="#fff"/><circle cx="23" cy="22" r="3" fill="#fff"/><circle cx="32" cy="28" r="3" fill="#fff"/><circle cx="42" cy="12" r="3" fill="#fff"/>
        </svg>
      </span>
      <span class="keyword-label">Normal Blood<br>Sugar Range</span>
      <span class="keyword-go"><svg viewBox="0 0 22 22" fill="none" stroke="#fff" stroke-width="3" stroke-linecap="round" stroke-linejoin="round" aria-hidden="true"><path d="M4 11h13M12 5l6 6-6 6"/></svg></span>
    </a>

    <a class="keyword chart" href="#">
      <span class="keyword-tile">
        <svg viewBox="0 0 50 50" aria-hidden="true">
          <rect x="6" y="28" width="8" height="16" rx="2" fill="#fff"/>
          <rect x="18" y="18" width="8" height="26" rx="2" fill="#fff"/>
          <rect x="30" y="24" width="8" height="20" rx="2" fill="#fff"/>
          <path d="M4 46H46" stroke="#fff" stroke-width="2.6" stroke-linecap="round"/>
          <path d="M40 4 C36 10 33 13 33 17 a7 7 0 0 0 14 0 C47 13 44 10 40 4Z" fill="#fff"/>
        </svg>
      </span>
      <span class="keyword-label">Blood Sugar<br>Levels Chart</span>
      <span class="keyword-go"><svg viewBox="0 0 22 22" fill="none" stroke="#fff" stroke-width="3" stroke-linecap="round" stroke-linejoin="round" aria-hidden="true"><path d="M4 11h13M12 5l6 6-6 6"/></svg></span>
    </a>

    <a class="keyword normal" href="#">
      <span class="keyword-tile">
        <svg viewBox="0 0 50 50" aria-hidden="true">
          <path d="M25 4 C19 15 11 23 11 33 a14 14 0 0 0 28 0 C39 23 31 15 25 4Z" fill="#fff"/>
          <path d="M18 33 a7 7 0 0 0 5 7" fill="none" stroke="var(--violet)" stroke-width="2.6" stroke-linecap="round"/>
        </svg>
      </span>
      <span class="keyword-label">What Is Normal<br>Blood Sugar</span>
      <span class="keyword-go"><svg viewBox="0 0 22 22" fill="none" stroke="#fff" stroke-width="3" stroke-linecap="round" stroke-linejoin="round" aria-hidden="true"><path d="M4 11h13M12 5l6 6-6 6"/></svg></span>
    </a>
  </nav>
</div>
</body>
</html>
```